Präsentationsvorlagen für die Cloud-Plattform LumaDesk
Zielgruppe
Ich bin ein unabhängiger Berater für die Cloud-Plattform LumaDesk. Zielgruppe sind Unternehmen jeglicher Größe. Das Design sollte schlicht und aufgeräumt sein.
Aufgabenstellung
Dunkler Hintergrund und die Farben aus dem Logo sollten enthalten sein.

```html
<!DOCTYPE html>
<html lang="en">
<head>
<meta charset="utf-8">
<title>Presentation Templates</title>
<link href="https://fonts.googleapis.com/css2?family=Lato:wght@400;700;900&display=swap" rel="stylesheet">
<style>
  :root {
    --page: #ffffff;
    --slide: #000000;
    --orange: #ed7d31;
    --blue: #0077b3;
    --light-blue: #bdd7ee;
    --text: #ffffff;
    --rule: #8a8a8a;
    --muted: #d9d9d9;
  }
  html, body {
    margin: 0;
    padding: 0;
    width: 1200px;
    height: 731px;
    overflow: hidden;
    background: var(--page);
  }
  .canvas {
    position: relative;
    width: 1200px;
    height: 731px;
  }
  .slide {
    position: absolute;
    width: 572px;
    height: 322px;
    background: var(--slide);
    display: block;
  }
  .slide--chart { left: 28px; top: 37px; }
  .slide--process { left: 610px; top: 37px; }
  .slide--mission { left: 28px; top: 363px; }
  .slide--closing { left: 610px; top: 363px; }
  text { font-family: 'Lato', sans-serif; fill: var(--text); }
  .title { font-weight: 900; font-size: 46px; }
  .subtitle { font-weight: 400; font-size: 17px; }
  .axis-label { font-size: 15px; letter-spacing: 1.5px; }
  .value-label { font-size: 11px; }
  .step-heading { font-weight: 700; font-size: 22px; }
  .body { font-size: 15px; }
  .section-heading { font-weight: 700; font-size: 19px; }
  .item-heading { font-weight: 700; font-size: 18px; }
  .brand-name { font-weight: 900; font-size: 58px; fill: var(--orange); }
  .thanks { font-weight: 900; font-size: 86px; }
  .button-label { font-weight: 700; font-size: 17px; }
  .bar--orange { fill: var(--orange); }
  .bar--blue { fill: var(--blue); }
  .bar--light { fill: var(--light-blue); }
  .chart-rule { stroke: var(--rule); stroke-width: 1.5; }
  .icon { fill: none; stroke: var(--orange); stroke-width: 3; stroke-linecap: round; stroke-linejoin: round; }
  .outline-icon { fill: none; stroke: var(--text); stroke-width: 2; }
</style>
</head>
<body>
<main class="canvas">

  <!-- Chart slide -->
  <svg class="slide slide--chart" viewBox="0 0 1175 661" aria-label="Chart diagram slide">
    <rect width="1175" height="661" fill="var(--slide)"/>
    <text class="title" x="586" y="126" text-anchor="middle">CHART DIAGRAM</text>
    <text class="subtitle" x="586" y="162" text-anchor="middle">PLEASE TITTLE TEXT HERE LOREM IPSUM</text>

    <g class="chart">
      <line class="chart-rule" x1="88" y1="225" x2="88" y2="573"/>
      <line class="chart-rule" x1="338" y1="225" x2="338" y2="573"/>
      <line class="chart-rule" x1="588" y1="225" x2="588" y2="573"/>
      <line class="chart-rule" x1="837" y1="225" x2="837" y2="573"/>
      <line class="chart-rule" x1="1087" y1="225" x2="1087" y2="573"/>
      <line class="chart-rule" x1="88" y1="573" x2="1087" y2="573"/>

      <!-- Category 1 -->
      <rect class="bar--orange" x="148" y="325" width="27" height="248"/>
      <rect class="bar--blue" x="199" y="435" width="27" height="138"/>
      <rect class="bar--light" x="250" y="458" width="27" height="115"/>
      <!-- Category 2 -->
      <rect class="bar--blue" x="398" y="429" width="27" height="144"/>
      <rect class="bar--orange" x="449" y="319" width="27" height="254"/>
      <rect class="bar--light" x="500" y="458" width="27" height="115"/>
      <!-- Category 3 -->
      <rect class="bar--orange" x="648" y="371" width="27" height="202"/>
      <rect class="bar--blue" x="699" y="469" width="27" height="104"/>
      <rect class="bar--light" x="750" y="400" width="27" height="173"/>
      <!-- Category 4 -->
      <rect class="bar--orange" x="897" y="314" width="27" height="259"/>
      <rect class="bar--blue" x="948" y="412" width="27" height="161"/>
      <rect class="bar--light" x="1000" y="285" width="27" height="288"/>

      <g class="value-labels">
        <text class="value-label" transform="translate(166 316) rotate(-90)">4.3</text>
        <text class="value-label" transform="translate(217 426) rotate(-90)">2.4</text>
        <text class="value-label" transform="translate(268 449) rotate(-90)">2</text>
        <text class="value-label" transform="translate(416 420) rotate(-90)">2.5</text>
        <text class="value-label" transform="translate(467 310) rotate(-90)">4.4</text>
        <text class="value-label" transform="translate(518 449) rotate(-90)">2</text>
        <text class="value-label" transform="translate(666 362) rotate(-90)">3.5</text>
        <text class="value-label" transform="translate(717 460) rotate(-90)">1.8</text>
        <text class="value-label" transform="translate(768 391) rotate(-90)">3</text>
        <text class="value-label" transform="translate(915 305) rotate(-90)">4.5</text>
        <text class="value-label" transform="translate(966 403) rotate(-90)">2.8</text>
        <text class="value-label" transform="translate(1018 276) rotate(-90)">5</text>
      </g>

      <text class="axis-label" x="213" y="598" text-anchor="middle">Category 1</text>
      <text class="axis-label" x="463" y="598" text-anchor="middle">Category 2</text>
      <text class="axis-label" x="712" y="598" text-anchor="middle">Category 3</text>
      <text class="axis-label" x="962" y="598" text-anchor="middle">Category 4</text>
    </g>
  </svg>

  <!-- Process slide -->
  <svg class="slide slide--process" viewBox="0 0 1175 661" aria-label="Infographic process slide">
    <rect width="1175" height="661" fill="var(--slide)"/>
    <text class="title" x="586" y="126" text-anchor="middle">INFOGRAPHIC PROSESS</text>
    <text class="subtitle" x="586" y="162" text-anchor="middle">PLEASE TITTLE TEXT HERE LOREM IPSUM DOLOR</text>

    <g class="connector" stroke="var(--rule)" stroke-width="1.5">
      <line x1="0" y1="332" x2="103" y2="332"/>
      <line x1="103" y1="290" x2="103" y2="375"/>
      <line x1="283" y1="290" x2="283" y2="375"/>
      <line x1="283" y1="332" x2="364" y2="332"/>
      <line x1="364" y1="290" x2="364" y2="375"/>
      <line x1="544" y1="290" x2="544" y2="375"/>
      <line x1="544" y1="332" x2="626" y2="332"/>
      <line x1="626" y1="290" x2="626" y2="375"/>
      <line x1="806" y1="290" x2="806" y2="375"/>
      <line x1="806" y1="332" x2="887" y2="332"/>
      <line x1="887" y1="290" x2="887" y2="375"/>
      <line x1="1067" y1="290" x2="1067" y2="375"/>
      <line x1="1067" y1="332" x2="1175" y2="332"/>
    </g>

    <g class="step-frames" fill="none" stroke="var(--orange)" stroke-width="2">
      <rect x="115" y="266" width="155" height="134"/>
      <rect x="376" y="266" width="155" height="134"/>
      <rect x="638" y="266" width="155" height="134"/>
      <rect x="899" y="266" width="155" height="134"/>
    </g>

    <!-- megaphone -->
    <g class="icon">
      <circle cx="175" cy="314" r="9"/>
      <path d="M165 366 v-30 q0-10 10-10 h10 l12-8"/>
      <path d="M197 310 l28-8 v26 l-28-8 z"/>
      <path d="M175 344 h10 v-10"/>
    </g>
    <!-- rocket -->
    <g class="icon">
      <path d="M486 300 q-28 4-42 34 l14 14 q30-14 28-48 z"/>
      <circle cx="469" cy="322" r="5"/>
      <path d="M446 330 l-14 4 l-6 10 l16-2"/>
      <path d="M462 346 l-4 14 l-10 6 l2-16"/>
      <path d="M438 356 l-10 10"/>
    </g>
    <!-- satellite -->
    <g class="icon">
      <path d="M700 296 l16 16 l-14 14 l-16-16 z"/>
      <path d="M730 310 l14 14 l-14 14 l-14-14 z"/>
      <path d="M744 324 l16 16 l-14 14 l-16-16 z"/>
      <path d="M706 336 q-10 10 0 22 l12-12"/>
    </g>
    <!-- dish -->
    <g class="icon">
      <path d="M956 302 q-10 36 26 48 z"/>
      <path d="M966 312 l28 -10 l-4 30"/>
      <path d="M962 340 l-12 26 h22 l-10-24"/>
    </g>

    <g class="step-text">
      <text class="step-heading" x="115" y="446">Lorem Ipsum</text>
      <text class="body" x="116" y="478">Lorem ipsum dolor sit</text>
      <text class="body" x="116" y="505">amet, consectetur adipis</text>
      <text class="body" x="116" y="531">cing elit sed do.</text>

      <text class="step-heading" x="376" y="446">Lorem Ipsum</text>
      <text class="body" x="377" y="478">Lorem ipsum dolor sit</text>
      <text class="body" x="377" y="505">amet, consectetur adipis</text>
      <text class="body" x="377" y="531">cing elit sed do.</text>

      <text class="step-heading" x="637" y="447">Lorem Ipsum</text>
      <text class="body" x="638" y="479">Lorem ipsum dolor sit</text>
      <text class="body" x="638" y="506">amet, consectetur adipis</text>
      <text class="body" x="638" y="532">cing elit sed do.</text>

      <text class="step-heading" x="899" y="446">Lorem Ipsum</text>
      <text class="body" x="900" y="478">Lorem ipsum dolor sit</text>
      <text class="body" x="900" y="505">amet, consectetur adipis</text>
      <text class="body" x="900" y="531">cing elit sed do.</text>
    </g>
  </svg>

  <!-- Mission slide -->
  <svg class="slide slide--mission" viewBox="0 0 1175 661" aria-label="Our mission slide">
    <defs>
      <linearGradient id="target-photo-tone" x1="0" y1="0" x2="1" y2="1">
        <stop offset="0" stop-color="#7a3a2a"/>
        <stop offset="0.45" stop-color="#e9a58a"/>
        <stop offset="1" stop-color="#dfe6ea"/>
      </linearGradient>
    </defs>
    <rect width="1175" height="661" fill="var(--slide)"/>
    <text class="title" x="119" y="142">OUR MISSION</text>
    <text class="subtitle" x="119" y="177">PLEASE TITTLE TEXT HERE LOREM IPSUM DOLOR</text>
    <text class="body" x="119" y="217">Lorem ipsum dolor sit amet, consectetur adipiscing</text>
    <text class="body" x="119" y="243">elit, sed do eiusmod tempor incididunt ut labore et</text>
    <text class="body" x="119" y="270">dolore magna aliqua. Ut enim ad minim.</text>

    <text class="section-heading" x="119" y="346">DECRIPTION TEXT HERE</text>

    <g class="outline-icon">
      <circle cx="135" cy="407" r="18"/>
      <circle cx="135" cy="407" r="13"/>
      <path d="M129 413 l3-9 l9-3 l-3 9 z"/>
    </g>
    <text class="item-heading" x="174" y="399">Lorem Ipsum Dolor</text>
    <text class="body" x="174" y="428">Lorem ipsum dolor sit amet, conse ctetur</text>
    <text class="body" x="174" y="454">adipiscing elit, sed do eius mod tempor.</text>

    <g class="outline-icon">
      <circle cx="134" cy="512" r="18"/>
      <circle cx="134" cy="512" r="11"/>
      <circle cx="134" cy="512" r="4"/>
      <path d="M134 512 l16-16 m0 0 v-6 m0 6 h6"/>
    </g>
    <text class="item-heading" x="174" y="506">Lorem Ipsum Dolor</text>
    <text class="body" x="174" y="533">Lorem ipsum dolor sit amet, conse ctetur</text>
    <text class="body" x="174" y="559">adipiscing elit, sed do eius mod tempor.</text>

    <rect x="577" y="0" width="11" height="661" fill="var(--orange)"/>
    <g role="img" aria-label="Photo of a hand holding a target with arrows in the bullseye">
      <rect x="588" y="0" width="587" height="661" fill="url(#target-photo-tone)"/>
    </g>
  </svg>

  <!-- Closing slide -->
  <svg class="slide slide--closing" viewBox="0 0 1175 661" aria-label="Thank you slide">
    <defs>
      <linearGradient id="portrait-tone" x1="0" y1="0" x2="0" y2="1">
        <stop offset="0" stop-color="#8c8a88"/>
        <stop offset="0.5" stop-color="#b08a74"/>
        <stop offset="1" stop-color="#2c3a5a"/>
      </linearGradient>
    </defs>
    <rect width="1175" height="661" fill="var(--slide)"/>
    <text class="brand-name" x="62" y="225">brightpath</text>

    <text class="thanks" x="57" y="382">THANK YOU</text>
    <text class="body" x="57" y="420">Lorem ipsum dolor sit amet, consectetur adipis cing elit sed do.</text>

    <rect x="0" y="499" width="25" height="57" fill="var(--blue)"/>
    <rect x="25" y="499" width="284" height="57" fill="var(--orange)"/>
    <text class="button-label" x="42" y="533">WWW.BRIGHTPATH-CLOUD.COM</text>

    <rect x="733" y="6" width="12" height="655" fill="var(--orange)"/>
    <g role="img" aria-label="Portrait photo of the consultant in a blue blazer">
      <rect x="745" y="0" width="430" height="661" fill="url(#portrait-tone)"/>
    </g>
  </svg>

</main>
</body>
</html>
```